Gym opening flyer

We need a flyer design for the opening/launch of our gym. We need the flyer ASAP. So we would like to choose the flyer as soon as possible. We will open the gym on Saturday, Feb 10. The flyer should have a front and back side

We would like to base the flyer on the following flyer (see link below) or something similar.

https://lumiqo.example/images/RtkWbz

I have also uploaded/attached our logo and pictures that we would like to use in our flyer. I have also attached a drawings of the front and back side of the flyer of what changes I would like (compared to the flyer in the link above).

You can use the text for Abour Us, Facilities from our webside www.vordo.example

Target Market(s)

Dubai, UAE

Industry/Entity Type

Fitness

Font styles to use
Other font styles liked:
• Primal

Requirements
Must have
• We need the design ASAP. We must have the Logo on the flyer and that we are opening on Feb 10th and that we have an open house between 10am to 7pm. We also need references to
• our website www.vordo.example
• Instagram @vordofit
• Facebook @vordofit
• Special offer that the flyer entitles the person to 3 free classes that is valid for one month until March 10, 2018.
Nice to have
• see above
Should not have
• see above

```html
<!DOCTYPE html>
<html lang="en">
<head>
<meta charset="UTF-8">
<title>Vordo Fitness – Grand Opening Flyer</title>
<link rel="stylesheet" href="https://fonts.googleapis.com/css2?family=Kaushan+Script&family=Montserrat:wght@800&family=Orbitron:wght@800&family=Source+Sans+3:wght@300;400;600&display=swap">
<style>
  :root {
    --panel-top: #3e534a;
    --panel-bottom: #22282a;
    --teal: #5ec4a0;
    --teal-text: #6cc8a5;
    --yellow: #f5e614;
    --white: #ffffff;
    --ink: #1e2324;
    --paper: #ffffff;
  }
  html, body {
    margin: 0;
    padding: 0;
    width: 1200px;
    height: 1200px;
    overflow: hidden;
    background: var(--paper);
  }
  .flyer {
    position: relative;
    width: 1200px;
    height: 1200px;
    background: var(--paper);
    font-family: "Source Sans 3", "Helvetica Neue", Arial, sans-serif;
  }
  .flyer__shapes { position: absolute; inset: 0; }
  .brand-badge {
    position: absolute;
    left: 216px;
    top: 48px;
    width: 152px;
    height: 152px;
    border-radius: 50%;
    background: var(--white);
    display: flex;
    align-items: center;
    justify-content: center;
    text-align: center;
    font-weight: 400;
    font-size: 22px;
    line-height: 1.1;
    color: var(--ink);
    letter-spacing: 1px;
  }
  .headline__script {
    position: absolute;
    font-family: "Kaushan Script", cursive;
    color: var(--yellow);
    margin: 0;
    line-height: 1;
    white-space: nowrap;
  }
  .headline__push { left: 548px; top: 32px; font-size: 74px; transform: rotate(-4deg); }
  .headline__fitness { left: 546px; top: 108px; font-size: 158px; transform: rotate(-6deg); }
  .headline__block {
    position: absolute;
    font-family: "Montserrat", Arial, sans-serif;
    font-weight: 800;
    color: var(--white);
    margin: 0;
    line-height: 1;
    white-space: nowrap;
  }
  .headline__to-new { left: 712px; top: 264px; font-size: 56px; }
  .headline__level { left: 738px; top: 322px; font-size: 56px; }
  .intro {
    position: absolute;
    left: 575px;
    top: 396px;
    width: 400px;
    margin: 0;
    color: var(--white);
    font-size: 17.4px;
    line-height: 25px;
    font-weight: 400;
  }
  .schedule {
    position: absolute;
    left: 598px;
    top: 526px;
    margin: 0;
    padding: 0;
    list-style: none;
  }
  .schedule__item {
    display: flex;
    align-items: center;
    height: 37.4px;
    color: var(--teal-text);
    font-size: 24.5px;
    font-weight: 400;
    white-space: pre;
  }
  .schedule__tick { width: 22px; height: 18px; margin-right: 10px; }
  .opening {
    position: absolute;
    left: 590px;
    top: 812px;
    width: 370px;
    text-align: center;
    color: var(--ink);
  }
  .opening__title {
    margin: 0 0 6px;
    font-family: "Orbitron", Arial, sans-serif;
    font-weight: 800;
    font-size: 30px;
    letter-spacing: 3px;
  }
  .opening__date, .opening__hours { margin: 0; font-size: 22px; line-height: 22px; }
  .free-classes {
    position: absolute;
    left: 600px;
    top: 962px;
    width: 420px;
    margin: 0;
    text-align: center;
    color: var(--ink);
    font-size: 19px;
    line-height: 24px;
    font-weight: 600;
  }
  .free-classes__valid { display: block; font-weight: 400; font-size: 17px; color: var(--teal); }
  .offer {
    position: absolute;
    left: 0;
    width: 1200px;
    text-align: center;
    margin: 0;
  }
  .offer__label {
    top: 1044px;
    font-family: "Orbitron", Arial, sans-serif;
    font-weight: 800;
    font-size: 22px;
    letter-spacing: 1.5px;
    color: var(--ink);
  }
  .offer__contact {
    top: 1070px;
    font-weight: 300;
    font-size: 39px;
    color: var(--teal);
    letter-spacing: 1px;
  }
  .address {
    position: absolute;
    left: 400px;
    top: 1130px;
    width: 404px;
    text-align: center;
    margin: 0;
    font-size: 17px;
    line-height: 26px;
    color: var(--white);
  }
  .socials {
    position: absolute;
    left: 0;
    top: 1168px;
    width: 1200px;
    margin: 0;
    text-align: center;
    font-size: 16px;
    line-height: 22px;
    color: var(--ink);
  }
</style>
</head>
<body>
<main class="flyer">
  <svg class="flyer__shapes" width="1200" height="1200" viewBox="0 0 1200 1200">
    <defs>
      <linearGradient id="panelGradient" x1="0" y1="0" x2="0" y2="1">
        <stop offset="0" stop-color="#3e534a"/>
        <stop offset="1" stop-color="#22282a"/>
      </linearGradient>
      <linearGradient id="athleteGradient" x1="0" y1="0" x2="0" y2="1">
        <stop offset="0" stop-color="#6b4a3c"/>
        <stop offset="0.45" stop-color="#3a2b26"/>
        <stop offset="1" stop-color="#1c1e20"/>
      </linearGradient>
    </defs>
    <polygon class="panel" points="130,0 1070,0 1070,932 130,712" fill="url(#panelGradient)"/>
    <polygon class="accent-band" points="238,228 360,208 482,985 192,990" fill="var(--teal)"/>
    <path class="athlete-photo" role="img" aria-label="Photo of a female athlete in black sportswear holding dumbbells, looking over her shoulder"
      d="M350,180 C400,160 450,190 460,240 C470,290 500,350 505,430 C515,520 520,620 515,720 C512,820 520,940 516,1032 L206,1032 C210,940 225,860 240,780 C250,700 252,620 262,540 C272,440 300,360 320,300 C330,250 320,200 350,180 Z"
      fill="url(#athleteGradient)"/>
    <g class="headline-arrow" stroke="var(--yellow)" stroke-width="4" fill="none" stroke-linecap="round">
      <line x1="522" y1="316" x2="690" y2="314"/>
      <line x1="552" y1="322" x2="692" y2="318"/>
      <polyline points="626,288 696,316 638,350"/>
      <polyline points="636,294 690,316 646,344"/>
    </g>
    <g class="opening-banner" fill="var(--yellow)">
      <polygon points="796,772 1010,756 966,748"/>
      <polygon points="580,800 948,774 968,928 598,910"/>
      <polygon points="672,922 748,944 746,926"/>
    </g>
    <polygon class="address-bar" points="394,1130 806,1124 804,1162 400,1152" fill="var(--ink)"/>
  </svg>

  <div class="brand-badge">VORDO<br>FITNESS</div>

  <p class="headline__script headline__push">Push your</p>
  <p class="headline__script headline__fitness">Fitness</p>
  <p class="headline__block headline__to-new">TO NEW</p>
  <p class="headline__block headline__level">LEVEL</p>

  <p class="intro">Vordo Fitness is a gym focused on circuit style training for all levels of fitness. We provide engaging and motivating group exercise classes that are both challenging and fun.</p>

  <ul class="schedule">
    <li class="schedule__item"><svg class="schedule__tick" viewBox="0 0 22 18"><polyline points="3,8 10,14 19,4" fill="none" stroke="var(--white)" stroke-width="4"/></svg>10 AM - GYM OPENS</li>
    <li class="schedule__item"><svg class="schedule__tick" viewBox="0 0 22 18"><polyline points="3,8 10,14 19,4" fill="none" stroke="var(--white)" stroke-width="4"/></svg>11 AM - VORDO DRILL</li>
    <li class="schedule__item"><svg class="schedule__tick" viewBox="0 0 22 18"><polyline points="3,8 10,14 19,4" fill="none" stroke="var(--white)" stroke-width="4"/></svg>1 PM   -  BODY FIT</li>
    <li class="schedule__item"><svg class="schedule__tick" viewBox="0 0 22 18"><polyline points="3,8 10,14 19,4" fill="none" stroke="var(--white)" stroke-width="4"/></svg>3 PM   -  CALORIE BURN</li>
    <li class="schedule__item"><svg class="schedule__tick" viewBox="0 0 22 18"><polyline points="3,8 10,14 19,4" fill="none" stroke="var(--white)" stroke-width="4"/></svg>7 PM   -  GYM CLOSES</li>
  </ul>

  <div class="opening">
    <p class="opening__title">GRAND OPENING</p>
    <p class="opening__date">Saturday, February 10</p>
    <p class="opening__hours">10 a.m. - 7 p.m.</p>
  </div>

  <p class="free-classes">This flyer entitles you to 3 FREE CLASSES<span class="free-classes__valid">Valid for one month until March 10, 2018</span></p>

  <p class="offer offer__label">SPECIAL OFFER – THIS FLYER</p>
  <p class="offer offer__contact">+971501234567 / VORDO.EXAMPLE / DUBAI</p>
  <p class="address">Corvel House 30th Floor - Harlan Heights - Dubai</p>
  <p class="socials">www.vordo.example &nbsp;·&nbsp; Instagram @vordofit &nbsp;·&nbsp; Facebook @vordofit</p>
</main>
</body>
</html>
```